"Trade with Tilda" needs a funky and stylish business card

Hi my name is Tilda, I am an experienced Bidnest Prime Vendor with a 100% satisfaction rating and over 400 items sold

My business name and bidnest username is "Trade with Tilda" I sell other peoples items on Bidnest for a commission. The main items I sell are furniture and renovation/building salvage items such as used kitchens, bathrooms , window doors etc.

I will be promoting my service in real estate agent offices, storage facilities, removalists, building and renovating companies.

i believe selling on bidnest is a great way for people to recycle their used goods and salvageable materials and reduce waste and landfill.

Target Market(s)

people selling their homes, renovators, builders, downsizers

Industry/Entity Type

Real Estate

Contact Information for Business Card

Tilda Marlowe
0492716045

Logo Text

Trade with Tilda

Logo styles of interest
Wordmark Logo
Requirements
Must have
• the business card must feature the bidnest logo mentioning primevendorr gold ranked vendor I have attached a copy
Nice to have
• i would like to have the trade with tilda logo written in royal blue

```html
<!DOCTYPE html>
<html lang="en">
<head>
<meta charset="utf-8">
<title>Trade with Tilda – Business Card</title>
<link rel="stylesheet" href="https://fonts.googleapis.com/css2?family=Open+Sans:wght@600;700&family=Arimo:wght@400&display=swap">
<style>
  :root {
    --backdrop: #1a1a1a;
    --paper: #f4f4f2;
    --royal-navy: #1b3470;
    --ink: #2a2a2a;
    --ink-soft: #555;
    --gold: #d9a52a;
    --white: #ffffff;
    --warm-orange: #e88a2a;
    --warm-pink: #d8286e;
    --cool-blue: #2a73b8;
  }
  * { box-sizing: border-box; margin: 0; padding: 0; }
  html, body {
    width: 1200px; height: 900px; overflow: hidden;
    background: var(--backdrop);
  }
  .canvas {
    width: 1200px; height: 900px;
    display: flex; align-items: center; justify-content: center; gap: 80px;
  }
  .card {
    width: 340px; height: 600px; position: relative; overflow: hidden;
    box-shadow: 0 12px 30px rgba(0,0,0,.5);
  }

  /* back side */
  .card--back { background: var(--warm-orange); }
  .card--back .artwork {
    position: absolute; inset: 0;
    background: linear-gradient(160deg, var(--warm-orange) 0%, var(--warm-pink) 55%, var(--cool-blue) 100%);
  }
  .card--back .seal {
    position: absolute; left: 50%; top: 50%;
    width: 190px; height: 190px; margin: -95px 0 0 -95px;
    border-radius: 50%; background: var(--royal-navy);
    display: flex; align-items: center; justify-content: center;
    padding: 0 20px;
  }
  .seal__name {
    font-family: "Open Sans", sans-serif; font-weight: 700;
    font-size: 18px; color: var(--white); text-align: center; line-height: 1.2;
    white-space: nowrap;
  }

  /* front side */
  .card--front { background: var(--paper); }
  .partner-mark {
    position: absolute; left: 36px; top: 40px;
    display: flex; align-items: center; gap: 8px;
  }
  .partner-mark__badge {
    width: 26px; height: 26px; border-radius: 50%; background: var(--gold);
  }
  .partner-mark__name {
    font-family: "Open Sans", sans-serif; font-weight: 700;
    font-size: 22px; color: var(--royal-navy);
  }
  .wordmark {
    position: absolute; left: 0; right: 0; top: 235px; text-align: center;
    font-family: "Open Sans", sans-serif; font-weight: 700;
    font-size: 34px; color: var(--royal-navy); letter-spacing: -.5px;
  }
  .contact {
    position: absolute; left: 36px; bottom: 46px;
  }
  .contact__head { display: flex; align-items: flex-end; gap: 6px; margin-bottom: 20px; }
  .contact__name {
    font-family: "Open Sans", sans-serif; font-weight: 700;
    font-size: 30px; color: var(--ink); line-height: 1;
  }
  .contact__role {
    font-family: "Open Sans", sans-serif; font-weight: 600;
    font-size: 10px; color: var(--ink); line-height: 1.2;
  }
  .contact__line {
    font-family: "Arimo", sans-serif; font-size: 16px;
    color: var(--ink-soft); line-height: 1.45; letter-spacing: .4px;
  }
</style>
</head>
<body>
<main class="canvas">
  <section class="card card--back">
    <div class="artwork" role="img" aria-label="Colourful swirling rainbow rays pattern"></div>
    <div class="seal"><span class="seal__name">Trade with Tilda</span></div>
  </section>

  <section class="card card--front">
    <div class="partner-mark">
      <span class="partner-mark__badge"></span>
      <span class="partner-mark__name">Bidnest</span>
    </div>
    <h1 class="wordmark">Trade with Tilda</h1>
    <div class="contact">
      <div class="contact__head">
        <p class="contact__name">Tilda</p>
        <p class="contact__role">Bidnest Prime Vendor</p>
      </div>
      <p class="contact__line">tradewithtilda@bidnest.com</p>
      <p class="contact__line">www.tradewithtilda.com</p>
      <p class="contact__line">www.bidnest.com</p>
      <p class="contact__line">Phone: 0492716045</p>
    </div>
  </section>
</main>
</body>
</html>
```